Corvelle Strategies business card

I need a business card for my new strategic consulting LLC, Corvelle Strategies. We specialize in helping people who care about broadband technology and telecommunications policy, and we're based in Washington DC. I'm looking for a card that says smart, credible, future-facing and signals a high level of expertise. It's DC, so there's clearly a limit to how crazy we can go with this card, but I am looking for a design that reflects a company that is comfortable with technology, policy, and having a little bit fun. I'm uploading my logo below, and I'd like to have it be part of the card design in some fashion.
Target Market(s)
Telecommunications and technology policy professionals
Industry/Entity Type
Technology policy
Contact Information for Business Card
Name of business, my name (Glen Mosswater), email (glen@corvellestrategies-example.com) , phone number (202-555-0148)phone number

```html
<!DOCTYPE html>
<html lang="en">
<head>
<meta charset="utf-8">
<title>Corvelle Strategies – Business Card</title>
<link rel="stylesheet" href="https://fonts.googleapis.com/css2?family=Montserrat:wght@400;500;800&display=swap">
<style>
  :root {
    --navy: #0b3d86;
    --navy-deep: #083a74;
    --navy-emboss: #06305f;
    --royal: #21448f;
    --orange: #f0a23b;
    --orange-rule: #ec8c2c;
    --ink: #0b2f66;
    --paper: #ffffff;
    --backdrop: #d9dadc;
  }
  * { box-sizing: border-box; margin: 0; padding: 0; }
  html, body {
    width: 1200px; height: 800px; overflow: hidden;
    background: var(--backdrop);
    font-family: "Montserrat", Arial, sans-serif;
  }
  .canvas { position: relative; width: 1200px; height: 800px; }

  .card {
    position: absolute;
    width: 560px; height: 320px;
    overflow: hidden;
    box-shadow: 0 10px 28px rgba(0,0,0,0.18);
  }

  /* Back side */
  .card--back {
    left: 70px; top: 90px;
    background: linear-gradient(135deg, var(--navy-deep), var(--navy));
    display: flex; align-items: center; justify-content: center; gap: 14px;
  }
  .card--back .brand-name {
    font-weight: 800; font-size: 40px; color: var(--navy-emboss);
    letter-spacing: 0.5px;
  }
  .card--back .brand-dot {
    width: 26px; height: 26px; border-radius: 50%; background: var(--orange);
  }

  /* Front side */
  .card--front {
    left: 570px; top: 390px;
    background: var(--paper);
  }
  .front-brand {
    position: absolute; right: 34px; top: 34px;
    display: flex; align-items: center; gap: 10px;
  }
  .front-brand .brand-name {
    font-weight: 800; font-size: 28px; color: var(--navy);
  }
  .front-brand .brand-dot {
    width: 22px; height: 22px; border-radius: 50%; background: var(--orange);
  }
  .front-band {
    position: absolute; right: 0; bottom: 0; width: 560px; height: 320px;
  }

  .contact-block { position: absolute; left: 40px; top: 150px; }
  .person-name { font-weight: 800; font-size: 26px; color: var(--navy); line-height: 1.1; }
  .person-title { font-weight: 500; font-size: 14px; color: var(--ink); margin-top: 4px; }
  .title-rule { width: 74px; height: 3px; background: var(--orange-rule); margin: 8px 0 12px; }
  .contact-list { list-style: none; }
  .contact-list li {
    display: flex; align-items: center; gap: 10px;
    font-size: 13.5px; color: var(--ink); margin-bottom: 7px;
  }
  .contact-list svg { width: 14px; height: 14px; flex: none; }
</style>
</head>
<body>
<main class="canvas">

  <section class="card card--back" aria-label="Card back">
    <span class="brand-name">Corvelle Strategies</span>
    <span class="brand-dot"></span>
  </section>

  <section class="card card--front" aria-label="Card front">
    <svg class="front-band" viewBox="0 0 560 320" aria-hidden="true">
      <path d="M250 320 C360 300 470 280 560 230 L560 320 Z" fill="var(--royal)"/>
    </svg>

    <div class="front-brand">
      <span class="brand-name">Corvelle Strategies</span>
      <span class="brand-dot"></span>
    </div>

    <div class="contact-block">
      <h1 class="person-name">Glen Mosswater</h1>
      <p class="person-title">Director</p>
      <div class="title-rule"></div>
      <ul class="contact-list">
        <li>
          <svg viewBox="0 0 24 24" aria-hidden="true"><path fill="var(--orange-rule)" d="M6.6 10.8a15.1 15.1 0 0 0 6.6 6.6l2.2-2.2a1 1 0 0 1 1-.25 11.4 11.4 0 0 0 3.6.57 1 1 0 0 1 1 1V20a1 1 0 0 1-1 1A17 17 0 0 1 3 4a1 1 0 0 1 1-1h3.5a1 1 0 0 1 1 1c0 1.25.2 2.45.57 3.57a1 1 0 0 1-.25 1z"/></svg>
          202-555-0148
        </li>
        <li>
          <svg viewBox="0 0 24 24" aria-hidden="true"><rect x="2" y="5" width="20" height="14" fill="var(--orange-rule)"/><path d="M2 5l10 8 10-8" fill="none" stroke="#fff" stroke-width="2"/></svg>
          glen@corvellestrategies-example.com
        </li>
        <li>
          <svg viewBox="0 0 24 24" aria-hidden="true"><g fill="none" stroke="var(--orange-rule)" stroke-width="2"><circle cx="12" cy="12" r="9"/><ellipse cx="12" cy="12" rx="4" ry="9"/><path d="M3 12h18M5 7h14M5 17h14"/></g></svg>
          corvellestrategies-example.com
        </li>
      </ul>
    </div>
  </section>

</main>
</body>
</html>
```